Card Design for my dog training business Rustpaw Obedience

Need a business card design for my dog training business with my new logo. Want the card to come off professional yet fun. Want it to be very eye catchy as well. I normally have these at vet clinics, pet stores, and groomers. so need it to look better than my competitors.
Target Market(s)
dog owners
Industry/Entity Type
Dog Training
Contact Information for Business Card
needs logo, my name and info
Font styles to use
Serif
Colors
0255a3
ffffff
ec1f27
000000
333333
fbfbfb
Requirements
Must have
- Rustpaw Obedience
- Hollis Brandt
- 415 903 2267
- info@rustpawobedience.example
- www.rustpawobedience.example

```html
<!DOCTYPE html>
<html lang="en">
<head>
<meta charset="utf-8">
<title>Rustpaw Obedience – Business Card</title>
<link href="https://fonts.googleapis.com/css2?family=Cormorant+Garamond:ital,wght@0,500;1,500&family=Open+Sans:wght@400;600&display=swap" rel="stylesheet">
<style>
  :root {
    --blue: #0255a3;
    --blue-light: #3b8fd0;
    --red: #ec1f27;
    --red-deep: #c4143f;
    --white: #ffffff;
    --paper: #fbfbfb;
    --ink: #000000;
    --grey: #333333;
    --stage: #e9e6e1;
    --art-tint: #eef3f9;
  }
  * { margin: 0; padding: 0; box-sizing: border-box; }
  html, body { width: 1200px; height: 1023px; overflow: hidden; }
  body {
    background: var(--stage);
    display: flex;
    flex-direction: column;
    align-items: center;
    justify-content: center;
    gap: 60px;
    font-family: "Open Sans", sans-serif;
  }
  .card {
    position: relative;
    width: 700px;
    height: 400px;
    border-radius: 4px;
    overflow: hidden;
    box-shadow: 0 6px 20px rgba(0,0,0,.18);
  }

  /* Front */
  .card-front {
    background: linear-gradient(90deg, var(--blue) 0%, var(--blue-light) 28%, var(--blue) 42%, var(--red-deep) 68%, var(--red) 100%);
  }
  .front-band {
    position: absolute;
    left: 230px;
    top: 0;
    width: 210px;
    height: 400px;
    background: var(--white);
  }
  .front-art {
    position: absolute;
    left: 270px;
    top: 40px;
    width: 380px;
    height: 320px;
    border-radius: 6px;
    background: linear-gradient(135deg, var(--white) 0%, var(--art-tint) 100%);
  }
  .front-brand {
    position: absolute;
    left: 40px;
    bottom: 40px;
    width: 170px;
    font-family: "Cormorant Garamond", serif;
    font-weight: 500;
    font-size: 32px;
    line-height: 1.05;
    color: var(--white);
  }

  /* Back */
  .card-back { background: var(--paper); }
  .back-brand {
    position: absolute;
    left: 50px;
    top: 44px;
    font-family: "Cormorant Garamond", serif;
    font-weight: 500;
    font-size: 28px;
    color: var(--ink);
    display: flex;
    align-items: center;
    gap: 10px;
  }
  .back-brand .mark {
    width: 14px; height: 14px; background: var(--ink);
  }
  .contact-list {
    position: absolute;
    left: 50px;
    top: 120px;
    list-style: none;
    font-size: 14px;
    color: var(--grey);
    line-height: 26px;
  }
  .contact-list li { display: flex; align-items: center; gap: 10px; }
  .contact-list svg { width: 12px; height: 12px; flex: none; }
  .tagline {
    position: absolute;
    left: 50px;
    top: 236px;
    font-family: "Cormorant Garamond", serif;
    font-style: italic;
    font-size: 24px;
    color: var(--blue);
  }
  .holder-name {
    position: absolute;
    right: 50px;
    bottom: 50px;
    font-size: 24px;
    font-weight: 400;
    letter-spacing: .5px;
    color: var(--blue);
  }
</style>
</head>
<body>

  <section class="card card-front">
    <div class="front-band"></div>
    <div class="front-art" role="img" aria-label="Line illustration of two dog heads in blue and red"></div>
    <div class="front-brand">Rustpaw Obedience</div>
  </section>

  <section class="card card-back">
    <div class="back-brand"><span class="mark"></span>Rustpaw Obedience</div>
    <ul class="contact-list">
      <li>
        <svg viewBox="0 0 12 12"><path d="M2 1 L4 1 L5 4 L3.5 5 A6 6 0 0 0 7 8.5 L8 7 L11 8 L11 10 A1 1 0 0 1 10 11 A9 9 0 0 1 1 2 A1 1 0 0 1 2 1 Z" fill="var(--red)"/></svg>
        415 903 2267
      </li>
      <li>
        <svg viewBox="0 0 12 12"><rect x="1" y="2.5" width="10" height="7" fill="var(--red)"/><path d="M1 2.5 L6 6.5 L11 2.5" stroke="var(--white)" fill="none"/></svg>
        info@rustpawobedience.example
      </li>
      <li>
        <svg viewBox="0 0 12 12"><circle cx="6" cy="6" r="5" fill="var(--red)"/><path d="M1 6 H11 M6 1 V11" stroke="var(--white)" stroke-width=".8"/></svg>
        www.rustpawobedience.example
      </li>
    </ul>
    <p class="tagline">“Training dogs across Texas one dog at a time.”</p>
    <h1 class="holder-name">HOLLIS BRANDT</h1>
  </section>

</body>
</html>
```